Business Card Design Project

for a second hand vintage clothing store. shop name is The Velvet Loft

Cards to be double sided

The name on the card is Marianne Trelford

Information to put on card:

The Velvet Loft
Marianne Trelford (no job title)
84/227 Quayle St, Pyrmont, Sydney, NSW, 2009.
Mobile: 0412 975 206
Email: thevelvetloft@mailbox-example.com.au
Web: www.thevelvetloft-example.com.au

Target Market(s)

Women looking at vintage clothing

Industry/Entity Type

Clothing

```html
<!DOCTYPE html>
<html lang="en">
<head>
<meta charset="utf-8">
<title>The Velvet Loft — Business Cards</title>
<link href="https://fonts.googleapis.com/css2?family=Source+Sans+3:wght@400&display=swap" rel="stylesheet">
<style>
  :root {
    --backdrop: #1c1c1e;
    --plum: #57242f;
    --cream: #f0dd9a;
    --amber: #e8902a;
    --rust: #c8461e;
    --ink-light: #f4ead6;
  }
  * { box-sizing: border-box; margin: 0; padding: 0; }
  html, body {
    width: 1200px; height: 1200px; overflow: hidden;
    background: var(--backdrop);
    font-family: "Source Sans 3", Arial, sans-serif;
  }
  .canvas { position: relative; width: 1200px; height: 1200px; }
  .card {
    position: absolute; left: 220px; width: 760px;
    background: var(--plum); overflow: hidden;
    box-shadow: 0 10px 30px rgba(0,0,0,.45);
  }
  .card--front { top: 110px; height: 440px; }
  .card--back { top: 630px; height: 450px; }
  .card__art { position: absolute; inset: 0; width: 100%; height: 100%; }
  .brand {
    position: absolute; display: flex; align-items: center; gap: 12px;
    color: var(--cream); font-weight: 400; white-space: nowrap;
    line-height: 1;
  }
  .brand__dot { width: 12px; height: 12px; border-radius: 50%; background: var(--cream); flex: none; }
  .card--front .brand { left: 250px; top: 172px; font-size: 46px; }
  .card--back .brand { left: 40px; top: 205px; font-size: 40px; }
  .contact {
    position: absolute; left: 405px; top: 160px;
    list-style: none; color: var(--ink-light);
    font-size: 16px; line-height: 34px;
  }
</style>
</head>
<body>
<main class="canvas">
  <section class="card card--front" aria-label="Card front">
    <svg class="card__art" viewBox="0 0 760 440" aria-hidden="true">
      <path fill="var(--cream)" d="M0,170 C180,200 260,300 420,300 C560,300 690,265 760,235 L760,250 C680,300 560,345 420,345 C240,345 150,260 0,250 Z"/>
      <path fill="var(--amber)" d="M0,282 C150,287 250,347 400,357 C470,362 520,358 560,352 C480,377 430,387 370,387 C230,387 140,342 0,357 Z"/>
    </svg>
    <div class="brand"><span class="brand__dot"></span>The Velvet Loft</div>
  </section>

  <section class="card card--back" aria-label="Card back">
    <svg class="card__art" viewBox="0 0 760 450" aria-hidden="true">
      <path fill="var(--cream)" d="M540,0 H760 V150 C720,80 650,25 540,0 Z"/>
      <path fill="var(--rust)" d="M665,0 H760 V150 C745,95 715,45 665,0 Z"/>
      <path fill="var(--plum)" d="M700,0 H760 V95 C745,60 728,28 700,0 Z"/>
      <path fill="var(--rust)" d="M760,300 C742,360 705,410 650,450 H760 Z"/>
    </svg>
    <div class="brand"><span class="brand__dot"></span>The Velvet Loft</div>
    <ul class="contact">
      <li>The Velvet Loft</li>
      <li>Marianne Trelford</li>
      <li>84/227 Quayle St, Pyrmont, Sydney, NSW, 2009.</li>
      <li>Mobile: 0412 975 206</li>
      <li>Email: thevelvetloft@mailbox-example.com.au</li>
      <li>Web: www.thevelvetloft-example.com.au</li>
    </ul>
  </section>
</main>
</body>
</html>
```